Granite Ridge Response Business Card

Side 1: Granite Ridge Response Logo (logo without Maltese cross) with industrial rope rescue related theme. Our company services - TRAINING - Fire Training, Confined Space Rescue Training, Rope Rescue training, Hazmat Training, Incident Command, EMS, Pump Operations Training. Website - graniteridgeresponse.example.
Side 2: Granite Ridge Response Fire Department Logo (logo with Maltese cross) with Firefighter related theme. Company (division) services - FIELD SERVICES - Fire Department, Stand-by Rescue, Safety, EMS, Planning. "Supporting the Emergency Response Community Since 1967"

Add contact information wherever it makes since (Name, Email, Phone).
I would like it to represent the Granite Ridge Response Fire Department Logo as a division not as a separate entity without saying it, possibly by depicting it in the background of Side 2 instead of being a standalone picture like the logo on Side 1.

```html
<!DOCTYPE html>
<html lang="en">
<head>
<meta charset="utf-8">
<title>Granite Ridge Response – Business Cards</title>
<link rel="stylesheet" href="https://fonts.googleapis.com/css2?family=Arimo:wght@400;700&display=swap">
<style>
  :root {
    --backdrop: #d9d9d9;
    --card: #ffffff;
    --ink: #1a1a1a;
    --accent: #e8401c;
    --accent-soft: #f08a6c;
    --muted: #555555;
    --card-w: 560px;
    --card-h: 320px;
  }
  * { box-sizing: border-box; margin: 0; padding: 0; }
  html, body { width: 1200px; height: 863px; overflow: hidden; }
  body {
    background: var(--backdrop);
    font-family: "Arimo", Arial, sans-serif;
    color: var(--ink);
    position: relative;
  }
  .card {
    position: absolute;
    width: var(--card-w);
    height: var(--card-h);
    background: var(--card);
    box-shadow: 0 6px 18px rgba(0,0,0,.15);
  }
  .card--training { left: 590px; top: 70px; }
  .card--field { left: 50px; top: 470px; }

  .divider { position: absolute; left: 0; top: 0; width: 100%; height: 100%; pointer-events: none; }

  .bullets { position: absolute; list-style: none; font-size: 15px; line-height: 1.2; }
  .bullets li { display: flex; align-items: center; gap: 7px; }
  .bullets li::before { content: ""; width: 7px; height: 7px; background: var(--accent); flex: none; }

  .training__heading {
    position: absolute; left: 330px; top: 34px;
    font-size: 19px; font-weight: 700; color: var(--accent); letter-spacing: .5px;
  }
  .bullets--left { left: 26px; top: 22px; }
  .bullets--right { left: 380px; top: 150px; }

  .brand {
    position: absolute; display: flex; align-items: center; gap: 8px;
    font-weight: 700; text-transform: uppercase; letter-spacing: 1.5px;
  }
  .brand__mark { width: 14px; height: 14px; flex: none; }
  .brand--training { left: 170px; top: 192px; color: var(--accent-soft); font-size: 19px; }
  .brand--training .brand__mark { background: var(--accent-soft); }
  .website { position: absolute; left: 170px; top: 240px; font-size: 18px; }

  .brand--field { left: 50px; top: 38px; color: var(--ink); font-size: 20px; }
  .brand--field .brand__mark { background: var(--accent); }
  .tagline { position: absolute; left: 50px; top: 72px; font-size: 11px; font-weight: 700; }

  .person { position: absolute; right: 36px; top: 48px; text-align: right; }
  .person__name { font-size: 19px; font-weight: 700; }
  .person__name span { color: var(--accent); }
  .person__role { font-size: 13px; }

  .contact { position: absolute; display: flex; align-items: center; gap: 6px; font-size: 16px; }
  .contact svg { flex: none; }
  .contact--phone { left: 36px; top: 140px; }
  .contact--email { left: 250px; top: 172px; }

  .field__heading { position: absolute; left: 36px; top: 218px; font-size: 14px; font-weight: 700; }
  .services {
    position: absolute; left: 36px; top: 246px; right: 20px;
    list-style: none; display: flex; flex-wrap: wrap; gap: 4px 12px;
    font-size: 15px; color: var(--accent);
  }
  .services li { display: flex; align-items: center; gap: 6px; }
  .services li::before { content: ""; width: 7px; height: 7px; background: var(--ink); }
</style>
</head>
<body>

  <section class="card card--training" aria-label="Training side">
    <svg class="divider" viewBox="0 0 560 320" aria-hidden="true">
      <polyline points="0,118 300,118 330,150 560,150" fill="none" stroke="#1a1a1a" stroke-width="2"/>
      <polyline points="0,125 297,125 327,157 560,157" fill="none" stroke="#e8401c" stroke-width="2"/>
    </svg>
    <ul class="bullets bullets--left">
      <li>Fire Training</li>
      <li>Confined Space Rescue Training</li>
      <li>Rope Rescue Training</li>
      <li>Hazmat Training</li>
    </ul>
    <h2 class="training__heading">TRAINING</h2>
    <ul class="bullets bullets--right" style="top:68px">
      <li>Incident Command</li>
      <li>EMS</li>
      <li>Pump Operations Training</li>
    </ul>
    <div class="brand brand--training"><span class="brand__mark"></span>Granite Ridge Response</div>
    <p class="website">www.graniteridgeresponse.example</p>
  </section>

  <section class="card card--field" aria-label="Field services side">
    <svg class="divider" viewBox="0 0 560 320" aria-hidden="true">
      <polyline points="0,98 260,116 290,108 560,126" fill="none" stroke="#e8401c" stroke-width="2"/>
      <polyline points="0,104 258,122 290,114 560,132" fill="none" stroke="#1a1a1a" stroke-width="2"/>
    </svg>
    <div class="brand brand--field"><span class="brand__mark"></span>Granite Ridge Response</div>
    <p class="tagline">Supporting the Emergency Response Community Since 1967</p>
    <div class="person">
      <p class="person__name">Daniel <span>Harper</span></p>
      <p class="person__role">Director</p>
    </div>
    <p class="contact contact--phone">
      <svg width="12" height="14" viewBox="0 0 12 14" aria-hidden="true"><path d="M3 1 L5 4 L3.5 5.5 Q5 9 7.5 10.5 L9 9 L11.5 11 L10 13 Q2 11 1 2 Z" fill="#e8401c"/></svg>
      (555) 014 2290
    </p>
    <p class="contact contact--email">
      <svg width="16" height="11" viewBox="0 0 16 11" aria-hidden="true"><rect width="16" height="11" fill="#e8401c"/><polyline points="0,0 8,6 16,0" fill="none" stroke="#fff" stroke-width="1.2"/></svg>
      granite.ridge.response@example.com
    </p>
    <h3 class="field__heading">FIELD SERVICES</h3>
    <ul class="services">
      <li>Fire Department</li>
      <li>Stand-by Rescue</li>
      <li>Safety</li>
      <li>Planning</li>
      <li>EMS</li>
    </ul>
  </section>

</body>
</html>
```